Educational Management System User Interface (Vantro Design Concepts)

Hi,I require a 1-page design for an educational management system. The image attached shows all required elements and also their locations. I require the design to be based on vantro-styled interfaces using elements from: http://qelvo.hostrun.io/qelvo-kitset/ & http://layoutmintly.com/layout-template/admin . Side menu's should not be too large that they hide the main content of the page.
Sorry very slight addition to the design as per new uploaded file.
I like how the elements of the vantro hub page are seperated with the background colour and white boxes. This could maybe work in the design as per the uploaded image?
Thanks,
Melvin
Reason: Some designers have some submissions.

```html
<!DOCTYPE html>
<html lang="en">
<head>
<meta charset="utf-8">
<title>Ledra LMS – Group Discussion</title>
<link href="https://fonts.googleapis.com/css2?family=Open+Sans:wght@400;600;700&display=swap" rel="stylesheet">
<style>
:root{
  --bg:#efefef;
  --card:#ffffff;
  --line:#d9d9d9;
  --purple:#a43bbf;
  --purple-dark:#8b2aa6;
  --blue:#1a5fa8;
  --blue-deep:#0d56a0;
  --sky:#3fb3e6;
  --navy-date:#3b5b8c;
  --text:#333333;
  --muted:#8a8a8a;
  --link:#4aa3d8;
  --green:#1fa83a;
  --red:#e4472f;
  --grey-dot:#c9c9c9;
  --info:#62b6e4;
  --timeline:#d3cfcf;
}
*{box-sizing:border-box;margin:0;padding:0}
html,body{width:1200px;height:853px;overflow:hidden}
body{background:var(--bg);font-family:"Open Sans",Arial,sans-serif;color:var(--text);position:relative}
.abs{position:absolute}
.card{position:absolute;background:var(--card);border:1px solid var(--line)}
.photo{border-radius:50%;background:radial-gradient(circle at 50% 40%,#9a857c,#4a3c3a);border:3px solid #fff;box-shadow:0 0 0 1px var(--line)}

/* top bar */
.topbar{position:absolute;left:0;top:0;width:1200px;height:46px;background:linear-gradient(#ab40c6,var(--purple-dark))}
.brand{position:absolute;left:12px;top:11px;display:flex;align-items:center;gap:9px;color:#fff;font-weight:700;font-size:19px;letter-spacing:.5px}
.brand-dot{width:22px;height:22px;border-radius:50%;background:#fff}
.nav-icons{position:absolute;left:258px;top:11px;display:flex;gap:20px}
.nav-icons svg{width:30px;height:26px;fill:#fff}
.alerts{position:absolute;left:952px;top:10px;display:flex;gap:10px}
.alert{position:relative;width:26px;height:26px}
.alert svg{width:26px;height:26px;fill:#fff}
.alert .count{position:absolute;top:-3px;right:-2px;width:14px;height:14px;border-radius:50%;background:#e2665a;color:#fff;font-size:9px;font-weight:700;text-align:center;line-height:14px}
.user-name{position:absolute;right:60px;top:15px;color:#fff;font-size:13px;font-weight:600;white-space:nowrap}
.user-icon{position:absolute;left:1151px;top:7px;width:32px;height:32px;border-radius:50%;background:#fff}
.user-icon svg{width:32px;height:32px;fill:var(--purple)}

/* profile */
.profile{left:13px;top:72px;width:215px;height:97px}
.profile .photo{position:absolute;left:18px;top:10px;width:78px;height:78px}
.profile-name{position:absolute;left:103px;top:31px;color:var(--blue);font-size:14px}
.profile-role{position:absolute;left:107px;top:53px;font-size:10px;color:#555;display:flex;align-items:center;gap:5px}
.profile-role i{width:7px;height:7px;border-radius:50%;background:#118a5e}

/* side lists */
.panel-head{height:38px;border-bottom:1px solid var(--line);display:flex;align-items:center;gap:10px;padding-left:11px;color:var(--blue);font-size:14px;position:relative}
.panel-head svg{width:26px;height:20px}
.group-list li{list-style:none;height:49px;border-bottom:1px solid #e6e6e6;display:flex;align-items:center;padding-left:19px;font-size:10px;color:#444;position:relative}
.group-list li::before{content:"";width:9px;height:9px;border-radius:50%;background:var(--grey-dot);margin-right:16px}
.group-list li.active{border-left:2px solid var(--blue);padding-left:17px}
.group-list li.active::before{background:var(--blue-deep)}
.group-list li::after{content:"";position:absolute;right:11px;top:20px;width:7px;height:7px;border-right:2px solid #555;border-top:2px solid #555;transform:rotate(45deg)}
.btn{position:absolute;color:#fff;font-size:11px;font-weight:700;display:flex;align-items:center;justify-content:center;border-radius:2px;white-space:nowrap}
.btn-create{left:14px;top:264px;width:142px;height:33px;background:var(--sky);box-shadow:0 0 0 2px #a8dff5}
.btn-join{left:14px;top:313px;width:142px;height:33px;background:var(--blue-deep)}
.groups{left:13px;top:179px;width:215px;height:346px}
.community{left:13px;top:538px;width:215px;height:104px}
.community .group-list li{border:none;height:44px;font-size:12px;padding-left:13px}
.community .group-list li::before{background:var(--blue-deep);margin-right:14px}

/* breadcrumb */
.crumbs{left:260px;top:71px;font-size:14px;font-weight:600;color:#777}
.crumbs .c1{color:var(--blue)} .crumbs .c2{color:var(--purple)} .crumbs .c3{color:var(--blue)}
.resources-label{left:742px;top:71px;font-size:14px;font-weight:600;color:var(--blue)}
.resources-label span{color:var(--purple)}
.hamburger{left:886px;top:70px;width:20px;height:17px;background:linear-gradient(var(--blue) 0 4px,transparent 4px 6.5px,var(--blue) 6.5px 10.5px,transparent 10.5px 13px,var(--blue) 13px)}

/* composer */
.composer .photo{position:absolute;left:247px;top:169px;width:70px;height:70px}
.post-input{left:336px;top:167px;width:576px;height:98px}
.post-input p{position:absolute;left:9px;top:6px;font-size:12px;color:#999}
.post-input .bar{position:absolute;left:0;right:0;bottom:0;height:26px;background:#f6f6f6;border-top:1px solid #e6e6e6}

/* timeline */
.timeline{left:280px;top:286px;width:4px;height:359px;background:var(--timeline)}
.refresh{left:267px;top:266px;width:31px;height:31px}

/* posts */
.post{border-radius:3px}
.post-title{position:absolute;font-size:14px;color:#222;white-space:nowrap}
.post-date{position:absolute;font-size:10.5px;color:#999}
.post-body{position:absolute;font-size:11.5px;line-height:21px;color:#333}
.post-actions{position:absolute;right:18px;top:14px;display:flex;gap:20px;font-size:11px;color:var(--link)}
.tail{position:absolute;left:-10px;top:20px;width:18px;height:18px;background:#fff;border-left:1px solid var(--line);border-bottom:1px solid var(--line);transform:rotate(45deg)}
.post-one{left:338px;top:344px;width:574px;height:156px}
.post-two{left:422px;top:533px;width:490px;height:129px}

/* resources dropdown */
.resources{left:659px;top:100px;width:253px;height:227px;box-shadow:0 2px 4px rgba(0,0,0,.08)}
.resources::before{content:"";position:absolute;right:8px;top:-7px;width:12px;height:12px;background:#fff;border-left:1px solid var(--line);border-top:1px solid var(--line);transform:rotate(45deg)}
.res{position:absolute;width:80px;text-align:center;font-size:12px;color:#444}
.res svg{display:block;margin:0 auto 3px;height:44px;width:48px}

/* right column */
.members{left:943px;top:64px;width:237px;height:338px}
.member{display:flex;align-items:center;height:48px;padding-left:19px;font-size:11.5px;color:#777;position:relative}
.member .photo{width:27px;height:27px;border:none;box-shadow:none;margin-right:9px}
.member .status{position:absolute;right:22px;width:8px;height:8px;border-radius:50%}
.member.first{border-right:2px solid #8aa8c8}
.btn-showall{left:135px;top:299px;width:80px;height:25px;background:var(--blue-deep);font-size:13px;font-weight:400;border:1px solid #0a3e77}
.events{left:943px;top:421px;width:237px;height:344px}
.event{height:61px;border-bottom:1px solid #e3e3e3;position:relative;padding:13px 0 0 34px}
.event:last-child{border-bottom:none}
.event .dot{position:absolute;left:13px;top:18px;width:10px;height:10px;border-radius:50%;background:var(--grey-dot)}
.event.active{border-right:2px solid #8aa8c8}
.event.active .dot{background:var(--info)}
.event-title{font-size:12.5px;color:#333}
.event-date{font-size:12px;font-weight:700;color:var(--navy-date)}
.event .info{position:absolute;right:24px;top:18px;width:24px;height:24px;border-radius:50%;background:var(--info);color:#fff;font-weight:700;font-size:15px;text-align:center;line-height:24px}
.btn-leave{left:942px;top:779px;width:195px;height:33px;background:var(--blue-deep);font-size:11.5px}
</style>
</head>
<body>

<header class="topbar">
  <div class="brand"><span class="brand-dot"></span>Ledra LMS</div>
  <nav class="nav-icons">
    <svg viewBox="0 0 30 26"><path d="M15 2 2 14h4v11h7v-7h4v7h7V14h4z"/></svg>
    <svg viewBox="0 0 30 26"><path d="M4 4h22v21H4zM6 9v14h18V9zM8 11h3v3H8zm5 0h3v3h-3zm5 0h3v3h-3zM8 16h3v3H8zm5 0h3v3h-3zm5 0h3v3h-3z" fill-rule="evenodd"/><rect x="8" y="1" width="3" height="5"/><rect x="19" y="1" width="3" height="5"/></svg>
    <svg viewBox="0 0 30 26"><path d="M3 14l4-4 6 6L24 5l4 4-15 15z"/></svg>
    <svg viewBox="0 0 30 26"><path d="M2 5h9l2 3h12v3H8L4 23H2zM9 13h20l-5 11H4z"/></svg>
  </nav>
  <div class="alerts">
    <div class="alert"><svg viewBox="0 0 26 26"><path d="M2 7h22v16H2zm2 2v1l9 7 9-7V9z" fill-rule="evenodd"/></svg><span class="count">5</span></div>
    <div class="alert"><svg viewBox="0 0 26 26"><path d="M13 3c4 0 7 3 7 7v7l3 3H3l3-3v-7c0-4 3-7 7-7zm-3 19h6a3 3 0 0 1-6 0z"/></svg><span class="count">8</span></div>
  </div>
  <div class="user-name">MARISA DELVANE</div>
  <div class="user-icon"><svg viewBox="0 0 32 32"><circle cx="16" cy="12" r="6"/><path d="M5 26c2-6 6-8 11-8s9 2 11 8z"/></svg></div>
</header>

<aside>
  <section class="card profile">
    <div class="photo" role="img" aria-label="Profile photo of the teacher"></div>
    <div class="profile-name">MARISA</div>
    <div class="profile-role"><i></i>TEACHER</div>
  </section>

  <section class="card groups">
    <div class="panel-head"><svg viewBox="0 0 26 20" fill="none" stroke="#8a8a8a" stroke-width="1.3"><circle cx="8" cy="7" r="4"/><path d="M1 18c1-4 4-6 7-6s6 2 7 6z"/><circle cx="17" cy="7" r="4"/><path d="M15 12c4 0 7 2 9 6h-8"/></svg>MY GROUPS</div>
    <ul class="group-list">
      <li class="active">GROUP NAME ONE</li>
      <li>GROUP NAME TWO</li>
      <li>GROUP NAME THREE</li>
      <li>GROUP NAME FOUR</li>
    </ul>
    <div class="btn btn-create">+ CREATE NEW GROUP</div>
    <div class="btn btn-join">&gt; JOIN MORE GROUPS</div>
  </section>

  <section class="card community">
    <div class="panel-head"><svg viewBox="0 0 30 20" fill="#1a5fa8"><circle cx="7" cy="7" r="3.5"/><circle cx="15" cy="6" r="4"/><circle cx="23" cy="7" r="3.5"/><path d="M1 18c0-4 3-6 6-6s6 2 6 6zM9 18c0-5 3-7 6-7s6 2 6 7zM17 18c0-4 3-6 6-6s6 2 6 6z"/></svg>COMMUNITY</div>
    <ul class="group-list"><li>STUDY FINCH</li></ul>
  </section>
</aside>

<main>
  <div class="abs crumbs"><span class="c1">MY </span><span class="c2">GROUPS</span> &gt;&gt; The Corvane Group &gt;&gt; <span class="c3">Discussion</span></div>
  <div class="abs resources-label">GROUP <span>RESOURCES</span></div>
  <div class="abs hamburger"></div>

  <div class="composer">
    <div class="photo" role="img" aria-label="Photo of the signed-in teacher"></div>
    <div class="card post-input"><p>Please post your update</p><div class="bar"></div></div>
  </div>

  <div class="abs timeline"></div>
  <svg class="abs refresh" viewBox="0 0 31 31"><path d="M8 9a11 11 0 1 0 15 0" fill="none" stroke="#d3cfcf" stroke-width="3.5"/><path d="M15 3l-7 6 8 2z" fill="#d3cfcf"/></svg>

  <div class="photo abs" style="left:247px;top:331px;width:70px;height:70px" role="img" aria-label="Photo of post author"></div>
  <article class="card post post-one">
    <span class="tail"></span>
    <div class="post-title" style="left:19px;top:22px">Torren Ashby |&nbsp; 09:15 14/5/2014</div>
    <div class="post-actions"><span>Reply</span><span>Forward</span><span>Delete</span></div>
    <div class="post-date" style="left:23px;top:47px">Monday, may 5-, 2014</div>
    <p class="post-body" style="left:21px;top:70px;width:540px">"Lorem ipsum dolor sit amet, consectetur adipiscing elit, sed do eiusmod tempor incididunt ut labore et dolore magna aliqua. Ut enim ad minim veniam, quis nostrud exercitation ullamco laboris nisi ut aliquip ex ea commodo consequat.</p>
  </article>

  <div class="photo abs" style="left:337px;top:523px;width:62px;height:62px;background:radial-gradient(circle at 50% 45%,#c9a58a,#2f7d4f 70%)" role="img" aria-label="Photo of reply author"></div>
  <article class="card post post-two">
    <span class="tail"></span>
    <div class="post-title" style="left:22px;top:20px">Re: Torren Ashby |&nbsp; 09:15 14/5/2014</div>
    <div class="post-actions"><span>Reply</span><span>Forward</span><span>Delete</span></div>
    <div class="post-date" style="left:22px;top:41px">Monday, may 5-, 2014</div>
    <p class="post-body" style="left:21px;top:65px;width:460px">"Lorem ipsum dolor sit amet, consectetur adipiscing elit, sed do eiusmod tempor incididunt ut labore et dolore magna aliqua. Ut enim ad minim veniam, quis</p>
  </article>

  <section class="card resources">
    <div class="res" style="left:12px;top:16px"><svg viewBox="0 0 48 44"><path d="M20 2c10 0 18 7 18 15s-8 15-18 15l-8 8v-10C6 27 2 22 2 17 2 9 10 2 20 2z" fill="#1565b0"/><path d="M40 15c4 3 6 6 6 10 0 4-2 7-5 9v8l-7-6c-4 0-8-1-10-3 9 0 16-7 16-18z" fill="#1565b0"/></svg>Discussions</div>
    <div class="res" style="left:96px;top:16px"><svg viewBox="0 0 48 44"><rect x="6" y="4" width="32" height="36" fill="none" stroke="#9a3ab8" stroke-width="4"/><path d="M13 13h4M21 13h11M13 21h4M21 21h11M13 29h4M21 29h7" stroke="#9a3ab8" stroke-width="3"/><path d="M42 20l4 4-12 13-6 2 2-6z" fill="#9a3ab8"/></svg>Assignments</div>
    <div class="res" style="left:176px;top:16px"><svg viewBox="0 0 48 44"><circle cx="24" cy="21" r="19" fill="none" stroke="#1565b0" stroke-width="3"/><text x="24" y="31" text-anchor="middle" font-family="Open Sans,Arial,sans-serif" font-weight="700" font-size="27" fill="#1565b0">?</text></svg>Quizzes</div>
    <div class="res" style="left:12px;top:90px"><svg viewBox="0 0 48 44"><path d="M6 6h3v32H6zM12 18h6v20h-6zM21 10h6v28h-6zM30 22h6v16h-6zM6 38h36v3H6z" fill="#1565b0"/></svg>Polls</div>
    <div class="res" style="left:96px;top:90px"><svg viewBox="0 0 48 44"><path d="M8 2h16l8 8v22H8z" fill="#1565b0"/><path d="M20 12h16l8 8v22H20z" fill="#35a4e0"/></svg>Files</div>
    <div class="res" style="left:176px;top:90px"><svg viewBox="0 0 48 44"><path d="M24 1l5 4 6-1 2 6 5 3-2 6 2 6-5 3-2 6-6-1-5 4-5-4-6 1-2-6-5-3 2-6-2-6 5-3 2-6 6 1z" fill="#1565b0"/><circle cx="24" cy="19" r="8" fill="none" stroke="#fff" stroke-width="2"/><path d="M14 32l-4 11 6-3 3 4 3-9zM34 32l4 11-6-3-3 4-3-9z" fill="#1565b0"/></svg>Badges</div>
    <div class="res" style="left:12px;top:158px"><svg viewBox="0 0 48 44"><path d="M30 2l8 3-8 20H16l6-4zM10 27h24v4H10zM20 31h4v7h-4zM8 40h28v3H8zM6 22l4 5-4 13-3-1z" fill="#1565b0"/></svg>Seating Plan</div>
  </section>
</main>

<aside>
  <section class="card members">
    <div class="panel-head" style="height:42px;padding-left:14px;gap:10px"><svg viewBox="0 0 28 22" fill="#1a5fa8"><circle cx="16" cy="6" r="5"/><path d="M6 21c0-6 4-9 10-9s10 3 10 9z"/><circle cx="7" cy="8" r="4"/><path d="M0 20c0-5 3-7 7-7 1 0 2 0 3 1-3 1-5 3-5 6z"/></svg>GROUP MEMBERS
      <svg viewBox="0 0 24 24" style="position:absolute;right:18px;top:10px;width:24px;height:24px"><circle cx="12" cy="12" r="10" fill="none" stroke="#1fa83a" stroke-width="2.5"/><path d="M12 6v12M6 12h12" stroke="#1fa83a" stroke-width="3"/></svg></div>
    <div style="padding-top:7px">
      <div class="member first"><div class="photo" role="img" aria-label="Member photo"></div>Dorian Wexfield<span class="status" style="background:var(--green)"></span></div>
      <div class="member"><div class="photo" role="img" aria-label="Member photo"></div>Pell Marchetton<span class="status" style="background:var(--red)"></span></div>
      <div class="member"><div class="photo" role="img" aria-label="Member photo"></div>Ivo Kessler<span class="status" style="background:var(--green)"></span></div>
      <div class="member"><div class="photo" role="img" aria-label="Member photo"></div>Reid Calloway<span class="status" style="background:var(--green)"></span></div>
      <div class="member"><div class="photo" role="img" aria-label="Member photo"></div>Lon Padrick<span class="status" style="background:var(--grey-dot)"></span></div>
    </div>
    <div class="btn btn-showall">Show All &gt;</div>
  </section>

  <section class="card events">
    <div class="panel-head" style="padding-left:12px"><svg viewBox="0 0 24 24" style="width:24px;height:24px" fill="#1a5fa8"><path d="M2 4h20v19H2zM4 9v12h16V9zM6 11h3v3H6zm5 0h3v3h-3zm5 0h3v3h-3zM6 16h3v3H6zm5 0h3v3h-3zm5 0h3v3h-3z" fill-rule="evenodd"/></svg>UPCOMING GROUP EVENTS</div>
    <div class="event active"><span class="dot"></span><div class="event-title">Meeting in the canteen</div><div class="event-date">Apr 22, 2014 | 12:45 pm</div><span class="info">i</span></div>
    <div class="event"><span class="dot"></span><div class="event-title">Assignment One is due</div><div class="event-date">Apr 22, 2014 | 12:45 pm</div><span class="info">i</span></div>
    <div class="event"><span class="dot"></span><div class="event-title">New Quiz in Class room 1</div><div class="event-date">Apr 22, 2014 | 12:45 pm</div><span class="info">i</span></div>
    <div class="event"><span class="dot"></span><div class="event-title">Meeting in the canteen</div><div class="event-date">Apr 22, 2014 | 12:45 pm</div><span class="info">i</span></div>
    <div class="event"><span class="dot"></span><div class="event-title">New Quiz in Class room 2</div><div class="event-date">Apr 22, 2014 | 12:45 pm</div><span class="info">i</span></div>
  </section>

  <div class="btn btn-leave">&gt;&gt; REQUEST TO LEAVE GROUP</div>
</aside>

</body>
</html>
```